Postcard Design

I am a mortgage broker located in Michigan. I recently opened my own company after working for another for 7 years. I want to send out a mailing letting my old clients know my new information and also reach out to them to let me know if I can assist them with anything.

It Company

```html
<!DOCTYPE html>
<html lang="en">
<head>
<meta charset="UTF-8">
<title>Summit Lending – Postcard</title>
<link href="https://fonts.googleapis.com/css2?family=Open+Sans:wght@400;600;700&display=swap" rel="stylesheet">
<style>
  :root {
    --brand-blue: #2a6fc9;
    --band-blue-dark: #1f3f8a;
    --band-blue-light: #3e66b8;
    --panel-gray: #e4e6ea;
    --name-blue: #2f62b8;
    --text-dark: #1c1c1c;
    --line-gray: #c9c9c9;
    --photo-sky: #b9cde6;
    --photo-grass: #5f8a3a;
    --headshot: #6b6f78;
  }
  * { margin: 0; padding: 0; box-sizing: border-box; }
  html, body {
    width: 1200px; height: 927px; overflow: hidden; background: #ffffff;
    font-family: "Open Sans", Arial, sans-serif;
  }
  .postcard { position: relative; width: 1200px; height: 927px; }

  .front { position: absolute; left: 0; top: 0; width: 711px; height: 905px; }
  .house-photo {
    position: absolute; left: 0; top: 0; width: 711px; height: 403px;
    background: linear-gradient(180deg, var(--photo-sky) 0%, #d8d4c8 45%, #a89a85 70%, var(--photo-grass) 100%);
  }
  .message-band {
    position: absolute; left: 0; top: 403px; width: 711px; height: 165px;
    background: linear-gradient(180deg, var(--band-blue-light) 0%, var(--band-blue-dark) 100%);
    display: flex; align-items: center; justify-content: center;
  }
  .message-band p {
    color: #ffffff; font-size: 34px; line-height: 1.5; text-align: center; font-weight: 400;
  }
  .agent-panel {
    position: absolute; left: 0; top: 568px; width: 711px; height: 337px;
    background: var(--panel-gray);
  }
  .headshot {
    position: absolute; left: 37px; top: 62px; width: 190px; height: 225px;
    background: linear-gradient(180deg, #8a8f99 0%, var(--headshot) 60%, #2c3140 100%);
  }
  .agent-name {
    position: absolute; left: 280px; top: 78px;
    color: var(--name-blue); font-size: 27px; font-weight: 400; line-height: 1.2;
  }
  .agent-title {
    position: absolute; left: 280px; top: 112px;
    color: var(--name-blue); font-size: 20px; font-weight: 600;
  }
  .agent-contact {
    position: absolute; left: 280px; top: 160px;
    color: var(--text-dark); font-size: 20px; line-height: 25px; font-style: normal;
  }

  .brand-wrap { position: absolute; left: 750px; top: 74px; width: 250px; }
  .brand-mark {
    display: block; width: 46px; height: 46px; margin: 0 auto 14px; background: var(--brand-blue);
  }
  .brand {
    text-align: center; color: var(--brand-blue);
    font-size: 27px; font-weight: 700; letter-spacing: 0.5px; line-height: 1.2;
  }
  .stamp-box {
    position: absolute; left: 1030px; top: 9px; width: 159px; height: 152px;
    border: 2px solid var(--line-gray);
  }
  .address-lines { position: absolute; left: 793px; top: 326px; }
</style>
</head>
<body>
<div class="postcard">
  <section class="front">
    <div class="house-photo" role="img" aria-label="Photo of a large stone and stucco family home with a green lawn"></div>
    <div class="message-band">
      <p>We worked together before and<br>I would like to work together again</p>
    </div>
    <div class="agent-panel">
      <div class="headshot" role="img" aria-label="Portrait photo of the company president"></div>
      <h2 class="agent-name">Daniel Hartley</h2>
      <div class="agent-title">President</div>
      <address class="agent-contact">
        303-555-0142 | 303-555-0177<br>
        dan@summitlendinggroup<br>
        2450 W. Maple Ridge<br>
        Suite 305<br>
        Fairview, Co 80999
      </address>
    </div>
  </section>

  <div class="brand-wrap">
    <span class="brand-mark"></span>
    <div class="brand">SUMMIT LENDING</div>
  </div>
  <div class="stamp-box"></div>
  <svg class="address-lines" width="396" height="230" viewBox="0 0 396 230">
    <g stroke="#c9c9c9" stroke-width="2">
      <line x1="0" y1="1" x2="396" y2="1"/>
      <line x1="0" y1="46" x2="396" y2="46"/>
      <line x1="0" y1="92" x2="396" y2="92"/>
      <line x1="0" y1="136" x2="396" y2="136"/>
      <line x1="0" y1="180" x2="396" y2="180"/>
      <line x1="0" y1="224" x2="396" y2="224"/>
    </g>
  </svg>
</div>
</body>
</html>
```